Domain Search Page and Results

We are looking for creative methods to display a domain registration search page, with many extensions. We are only looking for designs of the inside of the page and not for the frame around the page.
There are currently 4 categories and after pressing submit there is the results: however in the future there will be more categories (around 7 or 8) and domain extensions.
We would like creative methods to display the different (7-8) categories and extensions and also the results display.
The categories should be open/close-able.
We are planning to use JQuery and your suggestions for any movement will be appreciated.
We also would like creative ways to display the results.
Thank you.
Additions:
- It is not necessary to change the template/frame of the page. We are only looking for the search AND results display.
- We are looking for creative ideas and not necessary judging based on the actual design.
- We are basing the winner on how creatively it will be possible to display the search function AND results display. And to display creatively 7 or 8 categories with 100''s of domain extensions. The more creative and yet still user friendly the search functionality is, the chances of being selected will be higher.
- There will be 7 or 8 categories (and not just 4 as in the sample). The design must be able to extend to 7 or 8 categories. In some categories there are over 100 extensions. Creative ideas on how to sub categorize the extensions will be a bonus.

```html
<!DOCTYPE html>
<html lang="en">
<head>
<meta charset="utf-8">
<title>Hinode Domains – Domain Search</title>
<link href="https://fonts.googleapis.com/css2?family=Montserrat:wght@400;600;700&family=Ubuntu:wght@400;500;700&display=swap" rel="stylesheet">
<style>
:root{
  --red:#c8000f;
  --red-dark:#9e000b;
  --red-line:#a3000c;
  --black:#111;
  --ink:#333;
  --muted:#555;
  --row:#f2f2f2;
  --row-alt:#f8f8f8;
  --white:#fff;
}
*{margin:0;padding:0;box-sizing:border-box}
html,body{width:697px;height:1200px;overflow:hidden;background:var(--white)}
body{position:relative;font-family:"Ubuntu",sans-serif;color:var(--ink)}
.abs{position:absolute}

/* header */
.site-header{left:0;top:0;width:697px;height:62px;background:linear-gradient(#fbfbfb,#e6e6e6);border-bottom:1px solid #d0d0d0}
.brand{left:72px;top:21px;display:flex;align-items:center;gap:6px;font:700 12px "Ubuntu",sans-serif;color:var(--black);white-space:nowrap}
.brand-dot{width:20px;height:20px;border-radius:50%;background:var(--red);flex:none}
.account-link{left:425px;top:10px;font:500 6px "Ubuntu",sans-serif;color:var(--black);letter-spacing:.2px}
.lang{top:9px;width:13px;height:9px;border:1px solid #ccc}
.lang-en{left:574px;background:#2b3f8c}
.lang-ja{left:592px;background:#fff}
.lang-ja::after{content:"";position:absolute;left:4px;top:1.5px;width:4px;height:4px;border-radius:50%;background:var(--red)}
.lang-zh{left:610px;background:#d8261c}
.main-nav{left:222px;top:33px;display:flex;font:700 8px "Montserrat",sans-serif;color:var(--black);white-space:nowrap}

/* hero */
.hero{left:0;top:62px;width:697px;height:210px;background:radial-gradient(ellipse at 70% 40%,#e00010,var(--red) 45%,#8d0009)}
.hero-title{left:94px;top:90px;width:220px;font:700 18.5px/20px "Ubuntu",sans-serif;color:var(--white)}
.hero-text{left:94px;top:176px;width:225px;font:400 7.4px/14px "Ubuntu",sans-serif;color:var(--white)}
.hero-art{left:348px;top:104px;width:241px;height:140px;border-radius:6px;background:linear-gradient(#eeeeee,#bdbdbd)}
.scroll-cue{left:324px;top:248px;width:48px;height:48px;border-radius:50%;background:var(--red);z-index:2}
.scroll-cue svg{position:absolute;left:17px;top:26px}

/* search band */
.search-band{left:0;top:272px;width:697px;height:242px;background:linear-gradient(160deg,#8a8480,#c9c2bc 45%,#a19890 70%,#6b5d55)}
.search-title{left:0;top:350px;width:697px;text-align:center;font:600 23px "Montserrat",sans-serif;color:var(--white);letter-spacing:.4px}
.search-bar{left:119px;top:390px;width:459px;height:41px;background:var(--black)}
.search-bar .placeholder{position:absolute;left:6px;top:16px;font:400 7.5px "Ubuntu",sans-serif;color:#666}
.search-bar .go{position:absolute;left:363px;top:7px;width:91px;height:28px;background:var(--red-dark);color:var(--white);font:700 10px/28px "Ubuntu",sans-serif;text-align:center}

/* section titles */
.section-title{left:68px;font:700 14px "Ubuntu",sans-serif;color:var(--black)}

/* accordion */
.categories{left:68px;top:555px;width:559px}
.cat{position:relative;height:28.4px;background:var(--red);border-bottom:1px solid var(--red-line);color:var(--white);font:700 10.5px/28px "Ubuntu",sans-serif;padding-left:10px}
.cat .btn{position:absolute;left:456px;top:4px;width:64px;height:20px;background:var(--black);font:500 7.5px/20px "Ubuntu",sans-serif;text-align:center}
.cat .toggle{position:absolute;left:537px;top:7px}
.extensions{height:39px;background:#eee;border:1px solid #ddd;border-top:0;display:flex;padding-left:33px;align-items:center;font:700 8px "Ubuntu",sans-serif;color:var(--black)}
.ext{display:flex;align-items:center;width:73.5px}
.box{display:inline-block;width:7px;height:7px;border:1px solid #2b4a8a;margin-right:6px;background:#fff;position:relative}
.box.on::after{content:"";position:absolute;left:1px;top:0;width:2px;height:4px;border:solid #2b8a50;border-width:0 1.5px 1.5px 0;transform:rotate(45deg)}

/* results */
.results{left:68px;top:866px;width:559px;border-collapse:collapse;border:1px solid #ccc}
.results th{height:37px;background:var(--red);color:var(--white);font:700 10px "Ubuntu",sans-serif;border-right:1px solid var(--red-line)}
.results th:first-child{text-align:left;padding-left:10px}
.results td{height:28px;border-top:1px solid #ddd;border-right:1px solid #e2e2e2;font:400 9.5px "Ubuntu",sans-serif;color:var(--muted);text-align:center}
.results tr:nth-child(odd) td{background:var(--row)}
.results tr:nth-child(even) td{background:var(--row-alt)}
.results td.domain{text-align:left;padding-left:10px;font-size:10.5px}
.results .box{margin:0}
.select-btn{display:inline-block;width:54px;height:18px;background:var(--black);color:var(--white);font:500 7.5px/18px "Ubuntu",sans-serif}

/* footer */
.social{top:1142px;width:32px;height:32px;border-radius:50%;background:var(--black)}
.copyright{left:0;top:1180px;width:697px;text-align:center;font:400 8px "Ubuntu",sans-serif;color:#666}
</style>
</head>
<body>

<header class="site-header abs">
  <div class="brand abs"><span class="brand-dot"></span>Hinode Domains</div>
  <div class="account-link abs">LOGIN HERE / CREATE A NEW ACCOUNT HERE</div>
  <span class="lang lang-en abs" role="img" aria-label="English"></span>
  <span class="lang lang-ja abs" role="img" aria-label="Japanese"></span>
  <span class="lang lang-zh abs" role="img" aria-label="Chinese"></span>
  <nav class="main-nav abs">
    <span style="width:46px">HOME</span>
    <span style="width:55px">PRICING</span>
    <span style="width:57px">SEARCH</span>
    <span style="width:36px">FAQ</span>
    <span style="width:96px">HOSTING IN JAPAN</span>
    <span style="width:59px">RESELLERS</span>
    <span>CONTACT US</span>
  </nav>
</header>

<section class="hero abs"></section>
<h1 class="hero-title abs">To search for multiple domains, please enter the domains in the textarea below.</h1>
<p class="hero-text abs">If the domain is available, you may continue to register the domain. If the domain is unavailable, please search for an alternate domain.<br>Hint: Make sure to check your company domain isn't already taken. Enter the domain below and press "Search Here".</p>
<div class="hero-art abs" role="img" aria-label="Laptop showing a pointing hand cursor with a circular arrow"></div>

<section class="search-band abs" role="img" aria-label="Close-up photo of a hand typing on a keyboard"></section>
<div class="scroll-cue abs"><svg width="14" height="9" viewBox="0 0 14 9"><path d="M2 2l5 5 5-5" fill="none" stroke="#fff" stroke-width="2.6"/></svg></div>
<h2 class="search-title abs">Domain Search Availabilty</h2>
<div class="search-bar abs"><span class="placeholder">Enter Your Domain Name</span><span class="go">Search</span></div>

<h2 class="section-title abs" style="top:528px">Select Your Domains</h2>
<div class="categories abs">
  <div class="cat">Japan Domains<span class="btn">Search</span>
    <svg class="toggle" width="14" height="14" viewBox="0 0 14 14"><circle cx="7" cy="7" r="7" fill="#fff"/><path d="M4 5.5l3 3 3-3" fill="none" stroke="#c8000f" stroke-width="1.8"/></svg></div>
  <div class="extensions">
    <span class="ext"><i class="box"></i>.jp</span>
    <span class="ext"><i class="box on"></i>.ne.jp</span>
    <span class="ext"><i class="box"></i>.co.jp</span>
    <span class="ext"><i class="box"></i>.gr.jp</span>
    <span class="ext"><i class="box"></i>.tokyo.jp</span>
    <span class="ext"><i class="box"></i>.osaka.jp</span>
    <span class="ext"><i class="box"></i>.kyoto.jp</span>
  </div>
  <div class="cat">Japan Regional Domains<span class="btn">Search</span><svg class="toggle" width="14" height="14" viewBox="0 0 14 14"><circle cx="7" cy="7" r="7" fill="#fff"/><path d="M5.5 4l3 3-3 3" fill="none" stroke="#c8000f" stroke-width="1.8"/></svg></div>
  <div class="cat">gTLD Domains<span class="btn">Search</span><svg class="toggle" width="14" height="14" viewBox="0 0 14 14"><circle cx="7" cy="7" r="7" fill="#fff"/><path d="M5.5 4l3 3-3 3" fill="none" stroke="#c8000f" stroke-width="1.8"/></svg></div>
  <div class="cat">cc TLD Domains<span class="btn">Search</span><svg class="toggle" width="14" height="14" viewBox="0 0 14 14"><circle cx="7" cy="7" r="7" fill="#fff"/><path d="M5.5 4l3 3-3 3" fill="none" stroke="#c8000f" stroke-width="1.8"/></svg></div>
  <div class="cat">Japan Regional 1 Domains<span class="btn">Search</span><svg class="toggle" width="14" height="14" viewBox="0 0 14 14"><circle cx="7" cy="7" r="7" fill="#fff"/><path d="M5.5 4l3 3-3 3" fill="none" stroke="#c8000f" stroke-width="1.8"/></svg></div>
  <div class="cat">Dummy 1 Domains<span class="btn">Search</span><svg class="toggle" width="14" height="14" viewBox="0 0 14 14"><circle cx="7" cy="7" r="7" fill="#fff"/><path d="M5.5 4l3 3-3 3" fill="none" stroke="#c8000f" stroke-width="1.8"/></svg></div>
  <div class="cat">Dummy 2 Domains<span class="btn">Search</span><svg class="toggle" width="14" height="14" viewBox="0 0 14 14"><circle cx="7" cy="7" r="7" fill="#fff"/><path d="M5.5 4l3 3-3 3" fill="none" stroke="#c8000f" stroke-width="1.8"/></svg></div>
  <div class="cat">Dummy 3 Domains<span class="btn">Search</span><svg class="toggle" width="14" height="14" viewBox="0 0 14 14"><circle cx="7" cy="7" r="7" fill="#fff"/><path d="M5.5 4l3 3-3 3" fill="none" stroke="#c8000f" stroke-width="1.8"/></svg></div>
</div>

<h2 class="section-title abs" style="top:840px">Search Results</h2>
<table class="results abs">
  <colgroup><col style="width:118px"><col style="width:162px"><col style="width:180px"><col style="width:99px"></colgroup>
  <thead><tr><th>Domain</th><th>Result</th><th>Check Domains Below</th><th>Select</th></tr></thead>
  <tbody>
    <tr><td class="domain">kiraso.jp</td><td>Available</td><td><i class="box"></i></td><td><span class="select-btn">Select</span></td></tr>
    <tr><td class="domain">kiraso.ne.jp</td><td>Available</td><td><i class="box"></i></td><td><span class="select-btn">Select</span></td></tr>
    <tr><td class="domain">kiraso.co.jp</td><td>Available</td><td><i class="box"></i></td><td><span class="select-btn">Select</span></td></tr>
    <tr><td class="domain">kiraso.gr.jp</td><td>Available</td><td><i class="box"></i></td><td><span class="select-btn">Select</span></td></tr>
    <tr><td class="domain">kiraso.tokyo.jp</td><td>Not Available</td><td><i class="box"></i></td><td><span class="select-btn">Select</span></td></tr>
    <tr><td class="domain">kiraso.com</td><td>Not Available</td><td><i class="box"></i></td><td><span class="select-btn">Select</span></td></tr>
    <tr><td class="domain">kiraso.net</td><td>Not Available</td><td><i class="box"></i></td><td><span class="select-btn">Select</span></td></tr>
    <tr><td class="domain">kiraso.asia</td><td>Not Available</td><td><i class="box"></i></td><td><span class="select-btn">Select</span></td></tr>
  </tbody>
</table>

<footer>
  <span class="social abs" style="left:315px" role="img" aria-label="Social link"></span>
  <span class="social abs" style="left:349px" role="img" aria-label="Social link"></span>
  <p class="copyright abs">© 2014 Company Name ,All Rights Reserved</p>
</footer>

</body>
</html>
```